Booklet for meditation CD to match existing CD cover

We need a design for a booklet that matches the meditation CD cover previously designed. It should look like it belongs to the CD as it will be inserted into the cover slot. I hope you can re-use some of the existing artwork. It should incorporate the logo and the text and probably the list of tracks as well. I have attached the original CD cover file, the logo file, photo file and the specs from the CD production company for the 8 page booklet. The spec also includes a cover spec. You can ignore that part. Please put all the text from the CD cover, as well as the track names and the credits from the CD cover into the booklet and the text describing the meditation in full which I have enclosed as a word file.

Target Market(s)

People interested in meditation and personal growth

Font styles to use
Serif

Colors
0555a3
876aae
a54499
e667a6
ee363c

Requirements
Must have
• must match the existing CD cover, must include logo and photo and text from CD cover
• Design, Fonts and colours should match CD cover.

```html
<!DOCTYPE html>
<html lang="en">
<head>
<meta charset="utf-8">
<title>The Flow of Being Meditation – Booklet</title>
<link rel="stylesheet" href="https://fonts.googleapis.com/css2?family=Cinzel:wght@400;600&family=Josefin+Sans:wght@300;400;600&display=swap">
<style>
:root{
  --board:#3a3a3a;
  --paper:#ffffff;
  --ink:#4a4a4a;
  --soft-ink:#6d6d6d;
  --orange:#e8892a;
  --purple:#876aae;
  --violet:#6a4f92;
  --magenta:#a54499;
  --pink:#e667a6;
  --rose-line:#e9b9cf;
  --grey-band:#8a8a8a;
  --label:#bdbdbd;
}
*{box-sizing:border-box;margin:0;padding:0}
html,body{width:1200px;height:3327px;overflow:hidden;background:var(--board)}
body{position:relative;font-family:"Josefin Sans",sans-serif;color:var(--ink)}
.page{position:absolute;background:var(--paper);overflow:hidden}
.page-frame{position:absolute;inset:12px;border:1px solid var(--rose-line);pointer-events:none}
.page-num{position:absolute;left:24px;bottom:20px;font-size:10px;color:var(--soft-ink)}
.board-label{position:absolute;font-size:12px;letter-spacing:1px;color:var(--label)}
.col-left{left:25px;width:555px}
.col-right{left:622px;width:555px}
.text-block{position:absolute;left:30px;right:30px;font-size:10.6px;line-height:1.42;color:var(--ink);font-weight:300}
.text-block p{margin-bottom:7px}
.stage{font-size:12px;font-weight:600;color:var(--orange);text-transform:uppercase;letter-spacing:.4px;margin:6px 0 5px}
.stage span{color:var(--ink)}
.photo{position:absolute}
.brand{font-family:"Josefin Sans",sans-serif;font-weight:600;color:var(--purple);display:flex;align-items:center;gap:6px}
.brand i{display:inline-block;width:14px;height:14px;border-radius:50%;background:var(--purple)}
/* back */
.back-title{position:absolute;left:38px;top:46px;font-family:"Cinzel",serif;font-size:34px;letter-spacing:5px;color:#555}
.back-lines{position:absolute;left:40px;top:100px;font-family:"Cinzel",serif;font-size:15px;line-height:1.8;letter-spacing:2px;color:#555}
.back-info{position:absolute;left:40px;top:250px;font-size:11px;line-height:1.5;letter-spacing:1px;color:#555;text-transform:uppercase}
/* front */
.front-title{position:absolute;left:0;right:0;top:42px;text-align:center;font-family:"Cinzel",serif;font-weight:600;font-size:42px;line-height:1.1;color:#fff;text-shadow:0 1px 4px rgba(60,20,60,.5)}
/* tracks */
.tracks-title{position:absolute;left:40px;top:56px;font-family:"Cinzel",serif;font-size:32px;letter-spacing:6px;color:#555}
.track-list{position:absolute;left:40px;top:108px;width:300px;list-style:none;font-size:10px;line-height:1.65;letter-spacing:.5px;text-transform:uppercase;color:#555}
.track-list li{display:flex;border-bottom:1px dotted #bbb}
.track-list li b{font-weight:400;flex:1}
.quote{position:absolute;left:40px;right:40px;bottom:34px;font-size:10px;font-weight:600;line-height:1.5;color:#555}
.quote span{display:block;text-align:right}
/* page 01 */
.intro-band{position:absolute;left:20px;top:20px;bottom:20px;width:200px;background:#f1eef3;border-right:4px solid var(--grey-band)}
.intro-band p{padding:24px 18px;font-size:16px;line-height:1.55;letter-spacing:2px;color:var(--violet);text-transform:uppercase}
/* page 04 header */
.chakra-head{position:absolute;left:20px;right:20px;top:20px;height:110px;background:linear-gradient(90deg,#6b6b6b,#a9a9a9)}
.chakra-head h2{position:absolute;left:18px;top:18px;width:330px;font-family:"Cinzel",serif;font-size:18px;font-weight:400;line-height:1.3;letter-spacing:1.5px;color:#fff}
/* page 08 */
.finale-photo h2{position:absolute;left:22px;top:22px;width:250px;font-family:"Cinzel",serif;font-size:17px;font-weight:400;line-height:1.6;letter-spacing:1.5px;color:#fff;text-transform:uppercase}
.label-box{position:absolute;right:30px;bottom:60px;width:175px;height:140px;background:#fff;border:1px solid #ddd;padding:12px;font-size:9px;line-height:1.4;color:var(--soft-ink)}
.label-box .brand{font-size:20px;margin:8px 0 6px;color:var(--magenta)}
</style>
</head>
<body>

<section class="page col-left" style="top:20px;height:545px;background:linear-gradient(160deg,#ffffff,#ececec)">
  <h1 class="back-title">A MEDITATION</h1>
  <p class="back-lines">TO OPEN TO ALL THAT YOU ARE<br>TO FLY HIGH IN YOUR LIFE<br>TO OPEN TO YOUR ROOTS<br>AND YOUR WINGS</p>
  <p class="back-info">If you want to find out<br>more about workshops<br>with Mara Lind, go to<br>www.maralind.com</p>
  <div class="brand" style="position:absolute;left:40px;top:330px;font-size:24px"><i></i>MaraLind</div>
  <div class="photo" role="img" aria-label="Black and white portrait of the meditation teacher" style="left:270px;top:250px;width:265px;height:280px;background:linear-gradient(160deg,#d6d6d6,#6e6e6e)"></div>
  <div class="photo" role="img" aria-label="Orange flower resting on stacked stones" style="left:40px;top:400px;width:150px;height:130px;background:radial-gradient(ellipse at 50% 30%,#f5a23a 0 28%,#555 60%,transparent 62%)"></div>
</section>
<span class="board-label" style="left:25px;top:574px">BACK</span>

<section class="page col-right" style="top:20px;height:545px;background:linear-gradient(180deg,#2f3a6e 0%,#7a5c9e 40%,#d98fb5 70%,#f2c2c9 100%)" role="img" aria-label="Tree with a meditating figure on a glowing globe under a purple sky">
  <h1 class="front-title">THE FLOW OF BEING<br>MEDITATION</h1>
  <div class="brand" style="position:absolute;left:222px;bottom:40px;font-size:15px;color:#fff;background:rgba(255,255,255,.2);padding:4px 8px"><i style="background:#fff"></i>MaraLind</div>
</section>
<span class="board-label" style="left:622px;top:574px">FRONT</span>

<section class="page col-left" style="top:595px;height:510px;background:linear-gradient(180deg,#fff,#f0f0f0)">
  <h2 class="tracks-title">TRACKS</h2>
  <ol class="track-list">
    <li><b>1. Shaking</b>6:56</li>
    <li><b>2. The flow of your wild energy</b>6:58</li>
    <li><b>3. Loving yourself</b>5:51</li>
    <li><b>4. Focussing the energy</b>1:14</li>
    <li><b>5. Centre of instinct</b>1:47</li>
    <li><b>6. Sacral chakra</b>2:52</li>
    <li><b>7. Power centre</b>2:02</li>
    <li><b>8. Heartchakra</b>2:47</li>
    <li><b>9. Throatchakra</b>2:26</li>
    <li><b>10. Centreofintuition</b>2:08</li>
    <li><b>11. Crownchakra</b>1:56</li>
    <li><b>12. Silence</b>2:00</li>
    <li><b>13. Receivingtheinfinite</b>5:04</li>
    <li><b>14. Silence</b>15:00</li>
    <li><b>15. Celebration of being</b>4:08</li>
  </ol>
  <div class="photo" role="img" aria-label="Orange flower on a stack of dark stones" style="left:385px;top:250px;width:135px;height:150px;background:radial-gradient(ellipse at 50% 25%,#f5a23a 0 26%,#4a4a4a 58%,transparent 60%)"></div>
  <p class="quote">"GROUNDED IN YOUR NATURE, INSPIRED BY THE LIGHT AND WITH YOUR HEART'S OPEN YES TO ALL THAT YOU ARE, YOU FEEL THE BLESSING OF THIS LIFE."<span>- MARA LIND</span></p>
</section>
<span class="board-label" style="left:25px;top:1115px">PAGE_00_TRACK</span>

<section class="page col-right" style="top:595px;height:510px">
  <div class="page-frame"></div>
  <div class="intro-band"><p>The meditation is in 7 stages that start with movement and move towards stillness.</p></div>
  <div class="text-block" style="left:240px;top:30px;font-size:11px">
    <p>For this meditation you'll need a space where you can move freely and preferably have a mattress or soft space for the second and third stages. You'll need a pillow for the second stage.</p>
    <p>The meditation is in 7 stages that start with movement and move towards stillness.</p>
    <p>The seven stages are:</p>
    <p>1 Shaking (standing)</p>
    <p>2 Exploring your wild energy (on the floor or mattress)</p>
    <p>3 Loving yourself (on the floor or mattress)</p>
    <p>4 Journeying up through each of the energy centres or chakras in the body (moving mid-way to standing)</p>
    <p>5 Receiving the energy of the infinite standing in that consciousness</p>
    <p>6 Guided back into sitting in meditation for 15 minutes</p>
    <p>7 Celebration and returning to your day</p>
  </div>
  <span class="page-num">Page 01</span>
</section>

<section class="page col-left" style="top:1135px;height:520px">
  <div class="page-frame"></div>
  <div class="text-block" style="top:28px">
    <h3 class="stage">First stage: <span>Shaking</span></h3>
    <p>Stand with your feet about hip distance apart, feet firmly planted on the floor. Let your knees be soft and begin to let your body bounce, generating the shaking from your knees so that everything from your pelvis upwards can move freely. Be aware of your body's limitations. It is not necessary to shake strongly; it can be a gentle movement. Don't shake violently. If anything hurts or you are concerned about your body, either make the movement more gentle or lie on the floor and shake your limbs or don't do it at all.</p>
    <p>Try to keep your whole upper body relaxed, letting go of any holding so that everything can shake freely. Shake everything that you are thinking and feeling. Bring everything down into your body so that your focus of attention is in your body's aliveness and not in your head. Let your belly, shoulders and jaw be loose. Let your mouth be a little open and relaxed. Let your breathing be as full and easy.</p>
    <p>For this stage, keep any sounds inside.</p>
    <h3 class="stage">Second stage: <span>Exploring your wild energy</span></h3>
    <p>It is easier to get into your wild nature if you let yourself be down on the floor so you can roll around, let go and move easily. During this stage you let your body be as wild, free and uninhibited as you can. Start by holding the pillow so that you can use your hands to squeeze it and claw into it. Your mouth may even be biting into the pillow. Make sure you let your hips move. Be uncensored. Let your body have the freedom to move in ways that would be outside its regular habits. Shake, wriggle, thrash, roll and kick, opening them only to be sure that you aren't going to hit anything. If you can, let your wild sounds come as well as your wild movements. If that would cause problems, direct your sounds into the pillow. This wild energy may have many different flavours, sometimes all at the same time. It could be wildly happy or angry or sexual.</p>
  </div>
  <span class="page-num">Page 02</span>
</section>

<section class="page col-right" style="top:1135px;height:520px">
  <div class="page-frame"></div>
  <div class="text-block" style="top:28px">
    <p>Allow whatever arises and let your body lead you. Beware of going into a repeated pattern of getting angry by beating up someone from the past. Be willing to discover all your energies, not just what you know. Be curious about what is going on in your body. Never mind about what is happening last time you did it; let today be new and discover yourself today. Give yourself permission to enjoy your uncensored, wild energy. Breathe fully. Move fully. Use your hands and jaw and pelvis to connect with your wildness.</p>
    <h3 class="stage">Third stage: <span>Loving yourself</span></h3>
    <p>Now that you've let your energy be wild, you'll likely feel a lot of energy running through you. Enjoy! Feel your life, your life energy – whatever shape, color, movement or temperature – flowing inside you. Let your focus move to soft, deep breathing so that you feel more of yourself. Embrace and befriend all that you discover within yourself. Move softly and gently, maybe stroking yourself as you breathe softly but fully as a way of saying a total yes to yourself. Enjoy your aliveness. You can relax and let go into the softness of your body. Keep your body gently moving.</p>
    <h3 class="stage">Fourth stage: <span>Journeying up through each of the energy centres or chakras in the body</span></h3>
    <p><b style="font-weight:600">FOCUSING:</b></p>
    <p>Begin by focusing all the energy in your body down at the base of your body. Imagine white light energy streaming down from your head, from your fingers, from your toes, down into the base of your body, the first chakra. Use your breath – like you would use breath to start a fire, giving the fire more oxygen; more air to bring your inner fire alive. Imagine you could breathe through the base of your trunk. You can guide the energy by visualizing it moving in your body or by sensing it and guiding it, or by physically stroking your body as if you were sweeping the energy to the base of your body.</p>
  </div>
  <span class="page-num">Page 03</span>
</section>

<section class="page col-left" style="top:1690px;height:520px">
  <div class="page-frame"></div>
  <div class="chakra-head">
    <h2>JOURNEYING UP THROUGH EACH OF THE ENERGY CENTRES OR CHAKRAS IN THE BODY..</h2>
    <div class="photo" role="img" aria-label="Seated meditating figure with coloured chakra points" style="right:20px;top:8px;width:110px;height:94px;background:radial-gradient(ellipse at 50% 60%,#e0d6ea 0 35%,transparent 60%)"></div>
  </div>
  <div class="text-block" style="top:142px">
    <h3 class="stage">1st chakra: <span>Instinct - Nature</span></h3>
    <p>You are bringing your total focus to the centre of instinct that sits at the base of your trunk. We're going on a journey through the chakras or energy centres of your body. Even if this is unfamiliar to you, allow yourself to focus your attention in each centre or chakra and imagine your breath is going there. The centre of instinct is at the very base of your body. It is associated with primal energy, an energy that wants to become life, that wants to live. It has a raw quality to it. Think of a lioness protecting her young or animals mating. It is pure instinct. It doesn't have any reflection or consideration in it. It's the beginning stage of life happening.</p>
    <h3 class="stage">2nd chakra: <span>Sacral - Sex</span></h3>
    <p>From there we move the energy up into the sacral centre. This is focused on your sexual nature, your wanting and reaching out to get what you want and to get pleasure. Breathing and focusing on the area of your sex will help you connect with this. There is nothing to do with the energy, just notice the life that is happening there and let it have its natural movement.</p>
    <h3 class="stage">3rd chakra: <span>Navel - Power</span></h3>
    <p>Then we move up to the centre of power. This is the area sometimes known as the hara in martial arts. It's just below the belly button...</p>
  </div>
  <span class="page-num">Page 04</span>
</section>

<section class="page col-right" style="top:1690px;height:520px">
  <div class="page-frame"></div>
  <div class="text-block" style="top:28px">
    <p>As you breathe and focus on this area you can connect with your own personal power, the power to stand in your own being as a man or woman and feel your strength there. Let yourself move to standing during this section if you have been down on the mattress or floor. Feel yourself standing on the ground on your human journey as man or woman.</p>
    <h3 class="stage">4th chakra: <span>Heart</span></h3>
    <p>The fourth centre is the heart chakra. Focus on your heart with your breath. Imagine and feel all the wild energies from the lower centres flowing up into your heart and your heart transforming all this wild crazy passionate energy into a calm, loving radiance that fills you and surrounds you giving you a sense of a deeper inner yes to yourself. Bask in this deep inner yes to yourself that the heart centre gives you when you tune into it and allow it to receive you in your totality. Feel into the boundlessness of your heart and its capacity to hold you, embrace you. Feel how your heart is so much greater than your wounds. And as you connect with your heart energy, feel the sense of an inner mother holding you, the mother of great compassion embracing you. Relax into this and receive this loving energy.</p>
    <h3 class="stage">5th chakra: <span>Throat</span></h3>
    <p>This deep inner yes to yourself moves up into your throat centre, the centre of your unique expression of being. It brings a yes to your voice, to your way of being and living yourself so that you can bring your gifts to the world. Feel into the freedom to live and give of yourself without fear, without censoring yourself, knowing you are good enough. Trusting that your gift is uniquely yours to give and is welcomed by existence.</p>
    <h3 class="stage">6th chakra: <span>Third eye - Intuition</span></h3>
    <p>And then let that energy of a yes to your being flow up into the centre of intuition, the point between your eyebrows...</p>
  </div>
  <span class="page-num">Page 05</span>
</section>

<section class="page col-left" style="top:2245px;height:515px">
  <div class="page-frame"></div>
  <div class="text-block" style="top:28px">
    <p>It's the gateway beyond your physical self, sometimes felt as a deep inner knowing or being in touch with divine wisdom. The more you pay attention to this point, entering into a deep listening, the more you will receive. Don't worry if you don't feel anything at first. It's a practice and it may be a sense that you haven't used in a while. Enter with curiosity into the possibility.</p>
    <h3 class="stage">7th chakra: <span>Crown</span></h3>
    <p>Whatever you find, you let that energy also move upwards to the crown of your head or just above it. Allow your attention to expand out beyond yourself, allowing that connection with spirit that you have known since the beginning of time. You may have had glimpses of this ground of consciousness that is beyond the physical realm. Allow yourself to be still, melting into this ethereal state just as a drop of rain dissolves into the ocean. Enter One-ness. No doing, no trying. Simply being with whatever arises as you allow your consciousness to expand.</p>
  </div>
  <div class="photo" role="img" aria-label="Silhouette of a person in a yoga tree pose by the sea at dusk" style="left:30px;right:30px;top:255px;height:200px;background:linear-gradient(180deg,#c9c9c9 0%,#9a9a9a 55%,#3e3e3e 100%)"></div>
  <span class="page-num">Page 06</span>
</section>

<section class="page col-right" style="top:2245px;height:515px">
  <div class="page-frame"></div>
  <div class="text-block" style="top:28px">
    <h3 class="stage">Fifth stage:</h3>
    <p>Receiving the energy of the infinite and standing in that consciousness and giving yourself the delicious gift of complete stillness without any movement for two minutes.</p>
    <h3 class="stage">Sixth stage:</h3>
    <p>You are guided back, grounding all this energy down into your physical body. Your body still alive from the earlier stages of your journey and still open to receive and be enriched by the Source of existence. Allow that flow of energy to enrich and enlighten your physical body, opening each centre in turn: your third eye, your throat, your heart, your power centre, your sex and your root chakra. Allow this flow of Spirit back into your being and into the earth beneath your feet, finding yourself one part of the infinite flow of existence. And feel the flow of your nature rising up to meet Spirit in one eternal, never-ending cycle. Stay alive to all that is moving in you and find your way into sitting in stillness.</p>
    <p>Sitting in meditation for 15 minutes.</p>
    <p>A word about sitting. To get the most out of any silent sitting meditation, it is recommended that you keep your spine upright as if there were an invisible thread from the crown of your head pulling upwards while your body remains relaxed. It is more important to be comfortable than to contort your body or force it into a position that doesn't let you relax. Ideally you will have three points making contact with the floor. If you know how to sit in the lotus position and can relax there, that's wonderful. If you can sit cross-legged supported by a cushion with both knees touching the floor, that works well. If you are balancing on your sit bones with nothing else to support you, you're probably going to end up slumping. In that case, it is usually better to either sit against a wall or sit in a chair or stand.</p>
  </div>
  <span class="page-num">Page 07</span>
</section>

<section class="page col-left" style="top:2795px;height:515px">
  <div class="page-frame"></div>
  <div class="photo finale-photo" role="img" aria-label="Silhouette of a woman dancing with open arms against a golden sunset" style="left:20px;right:20px;top:20px;height:310px;background:linear-gradient(180deg,#6a4a52 0%,#c9874a 55%,#f0b85a 75%,#3a2a2a 100%)">
    <h2>Finally, as the music brings you back to end your meditation, allow it to call you into the beauty of this moment, into a celebration of life and all that it gives you</h2>
  </div>
  <div class="text-block" style="top:345px">
    <h3 class="stage">Seventh stage: <span>Celebration and returning to your day</span></h3>
    <p>Finally, as the music brings you back to end your meditation, allow it to call you into the beauty of this moment, into a celebration of life and all that it gives you, and especially into a celebration of this wholeness, this totality of being that you are, here, now today. Take this out into your day.</p>
  </div>
  <span class="page-num">Page 08</span>
</section>

<section class="page col-right" style="top:2795px;height:515px">
  <div class="page-frame"></div>
  <div class="photo" role="img" aria-label="Pink misty sunset sky with birds over a lake" style="left:20px;right:20px;top:20px;height:150px;background:linear-gradient(180deg,#b88aa8 0%,#e3a7b8 60%,#f3d0d6 100%)"></div>
  <div class="text-block" style="top:185px;right:230px">
    <h3 class="stage">Background</h3>
    <p>We developed this meditation primarily to be used in workshops as the morning meditation but it can also be used very effectively at home. You may need to use pillows to muffle the sounds during the wild phase. The aim is to bring you into your body, connecting through movement with both your physical and emotional body and then using that vital and alive connection to open to an experience of Essence.</p>
    <h3 class="stage" style="color:var(--ink)">Intimacy, relationship &amp; tantra groups</h3>
    <p><b style="font-weight:600">WITH MARA LIND</b></p>
    <p>Mara Lind, together with her husband Henrik Vos, leads workshops on sexuality, intimacy and relationship that invite you to live yourself totally, to grow a deeper love for yourself, and to open to richer, more nourishing relationships.</p>
    <p>www.maralind.com</p>
  </div>
  <div class="label-box">
    All music composed, produced, recorded, mixed and mastered by
    <div class="brand"><i style="background:var(--magenta)"></i>SOLVANE</div>
    www.solvane.com<br>
    Lyrics and Vocals by Mara Lind<br>
    Tom Ashby: percussion on track 5<br>
    Eli Marsh: flute on track 9
  </div>
  <span class="page-num">Page 09</span>
</section>

</body>
</html>
```